Criação de Layout Web-Design para Marketing & Comunicação
" Fornecemos informação referente as empresas do brasil, com opção de filtro para os usuários que busca fornecedores ou clientes. E tempos o espaço para as publicidades "

```html
<!DOCTYPE html>
<html lang="pt-BR">
<head>
<meta charset="utf-8">
<title>Anuncie grátis — BuscaBrasil</title>
<link href="https://fonts.googleapis.com/css2?family=Open+Sans:ital,wght@0,400;0,600;0,700;1,400&display=swap" rel="stylesheet">
<style>
  :root {
    --page-bg: #ffffff;
    --canvas-bg: #f2f3f5;
    --brand-yellow: #f6c12b;
    --accent-orange: #f29a1f;
    --purple: #6b1a8f;
    --ink: #333333;
    --muted: #8a8a8a;
    --field-border: #d6d6d6;
    --button-grey: #595959;
    --footer-navy: #2a2c3a;
    --line: #e6e6e6;
  }
  * { box-sizing: border-box; margin: 0; padding: 0; }
  html, body { width: 1200px; height: 1200px; overflow: hidden; }
  body {
    font-family: "Open Sans", Arial, sans-serif;
    color: var(--ink);
    background: var(--page-bg);
    display: flex;
    flex-direction: column;
  }

  /* Header */
  .site-header {
    height: 120px;
    border-bottom: 1px solid var(--line);
    display: flex;
    align-items: flex-start;
    padding: 0 60px;
    gap: 40px;
  }
  .brand-tag {
    background: var(--brand-yellow);
    height: 64px;
    padding: 0 28px;
    display: flex;
    align-items: center;
    gap: 10px;
    border-radius: 0 0 10px 10px;
    font-weight: 700;
    font-size: 22px;
    color: var(--ink);
  }
  .brand-tag .brand-square { width: 14px; height: 14px; background: var(--ink); }
  .search-area { flex: 1; padding-top: 26px; }
  .search-bar { display: flex; gap: 10px; }
  .select-field, .search-input {
    height: 42px;
    border: 1px solid var(--field-border);
    border-radius: 3px;
    font-size: 13px;
    color: var(--muted);
    display: flex;
    align-items: center;
    justify-content: space-between;
    padding: 0 12px;
  }
  .select-field.state { width: 80px; }
  .select-field.city { width: 150px; }
  .search-input { flex: 1; }
  .chevron { width: 10px; height: 6px; }
  .search-button {
    background: var(--purple);
    color: #fff;
    font-weight: 700;
    font-size: 12px;
    letter-spacing: .5px;
    border: 0;
    width: 110px;
    height: 42px;
    border-radius: 3px;
  }
  .advanced-search {
    text-align: right;
    margin-top: 10px;
    margin-right: 120px;
    font-size: 12px;
    font-weight: 700;
    color: var(--purple);
  }

  /* Main */
  .content {
    flex: 1;
    display: flex;
    gap: 40px;
    padding: 30px 60px 40px 100px;
  }
  .signup { flex: 1; }
  .breadcrumb { font-size: 12px; color: var(--muted); margin-bottom: 14px; }
  .page-title {
    font-size: 30px;
    font-weight: 400;
    font-style: italic;
    border-left: 5px solid var(--accent-orange);
    padding-left: 10px;
    line-height: 1.1;
  }
  .page-lead { font-size: 13px; color: var(--muted); margin: 14px 0 26px; }
  .form-row { display: flex; gap: 12px; margin-bottom: 16px; }
  .form-field {
    flex: 1;
    height: 44px;
    border: 1px solid var(--field-border);
    border-radius: 22px;
    padding: 0 18px;
    font-size: 13px;
    color: var(--muted);
    display: flex;
    align-items: center;
    justify-content: space-between;
  }
  .form-field.narrow { flex: 0 0 150px; }
  .form-field.number { flex: 0 0 90px; }
  .form-field.wide { flex: 0 0 560px; }
  .checkbox-row { display: flex; align-items: center; gap: 10px; font-size: 13px; color: var(--muted); margin: 6px 0 18px; }
  .checkbox { width: 14px; height: 14px; border: 1px solid var(--field-border); }
  .submit-button {
    width: 100%;
    height: 48px;
    background: var(--button-grey);
    color: #fff;
    font-weight: 700;
    font-size: 13px;
    letter-spacing: .5px;
    border: 0;
    border-radius: 3px;
  }

  /* Ads */
  .ad-column { width: 280px; display: flex; flex-direction: column; gap: 22px; }
  .ad-slot { height: 150px; }
  .ad-park { background: linear-gradient(135deg, #2a7bd4, #0f3f8a); }
  .ad-hotel { background: linear-gradient(135deg, #e6a04a, #8a4a1f); }
  .ad-deals { background: linear-gradient(135deg, #1c2f78, #3d5fc9); }
  .ad-car { background: linear-gradient(135deg, #9bb7d6, #2f5f9e); }
  .ad-market { background: linear-gradient(135deg, #e34b2c, #f2c431); }

  /* Footer */
  .site-footer {
    height: 110px;
    background: var(--footer-navy);
    display: flex;
    align-items: center;
    justify-content: center;
    gap: 10px;
    color: #fff;
    font-weight: 700;
    font-size: 20px;
  }
  .site-footer .brand-square { width: 14px; height: 14px; background: #fff; }
</style>
</head>
<body>
  <header class="site-header">
    <div class="brand-tag"><span class="brand-square"></span>BuscaBrasil</div>
    <div class="search-area">
      <div class="search-bar">
        <div class="select-field state">SP <svg class="chevron" viewBox="0 0 10 6"><path d="M0 0 L5 6 L10 0" fill="#999"/></svg></div>
        <div class="select-field city">Cidade <svg class="chevron" viewBox="0 0 10 6"><path d="M0 0 L5 6 L10 0" fill="#999"/></svg></div>
        <div class="search-input">Digite o nome da empresa ou ramo de atividade</div>
        <button class="search-button">PROCURAR</button>
      </div>
      <div class="advanced-search">BUSCA AVANÇADA</div>
    </div>
  </header>

  <main class="content">
    <section class="signup">
      <p class="breadcrumb">Home &gt; Anuncie grátis</p>
      <h1 class="page-title">Anuncie grátis!</h1>
      <p class="page-lead">Cadastre-se preenchendo os campos abaixo:</p>

      <div class="form-row"><div class="form-field">CNPJ*</div></div>
      <div class="form-row"><div class="form-field">Nome da empresa*</div></div>
      <div class="form-row">
        <div class="form-field narrow">Telefone*</div>
        <div class="form-field">E-mail*</div>
      </div>
      <div class="form-row">
        <div class="form-field narrow">Estado de interesse* <svg class="chevron" viewBox="0 0 10 6"><path d="M0 0 L5 6 L10 0" fill="#999"/></svg></div>
        <div class="form-field">Cidade de interesse* <svg class="chevron" viewBox="0 0 10 6"><path d="M0 0 L5 6 L10 0" fill="#999"/></svg></div>
      </div>
      <div class="form-row">
        <div class="form-field">Endereço*</div>
        <div class="form-field number">Nº*</div>
      </div>
      <label class="checkbox-row"><span class="checkbox"></span>Quero destacar o meu negócio</label>
      <button class="submit-button">CADASTRAR</button>
    </section>

    <aside class="ad-column">
      <div class="ad-slot ad-park" role="img" aria-label="Banner publicitário de parque de diversões"></div>
      <div class="ad-slot ad-hotel" role="img" aria-label="Banner publicitário de hotel com desconto"></div>
      <div class="ad-slot ad-deals" role="img" aria-label="Banner publicitário de ofertas exclusivas"></div>
      <div class="ad-slot ad-car" role="img" aria-label="Banner publicitário de automóvel"></div>
      <div class="ad-slot ad-market" role="img" aria-label="Banner publicitário de supermercado"></div>
    </aside>
  </main>

  <footer class="site-footer"><span class="brand-square"></span>BuscaBrasil</footer>
</body>
</html>
```